Fairway Nine Golf New Location Postcard

Design a double sided postcard, one side advertising our coaching program which includes 2 lessons a month with tour quality technology (Brightlane VX9, Arcmotion Replay Studio, and ROLO GreenDesk) and access to practice. 6months $2500 and 12months $4500. Special, pre-pay for a full-year program before the new year and save $500. <br/><br/>And the other side advertising our indoor practice membership which includes access to practice indoors rain or shine with the use of Flightbox (combine practice, virtual driving range and golf courses) $200/month unlimited practice sessions. Special, pre-pay for the year and save $400 plus get 24/7 access to practice. <br/><br/>Our new location is opening January 2020, 4215B Marrow Hollis Avenue. For more information and to sign up contact us at info@fairwayninegolf.example. www.fairwayninegolf.example. 513-862-7305

Font styles to use
Serif

Colors
ec1f27
ffffff

Requirements
Must have
• Logo. see attached image

```html
<!DOCTYPE html>
<html lang="en">
<head>
<meta charset="utf-8">
<title>Fairway Nine Golf – New Location Postcard</title>
<link rel="stylesheet" href="https://fonts.googleapis.com/css2?family=Open+Sans:wght@400;600;700;800&family=Oswald:wght@400;500;600&family=Anton&display=swap">
<style>
  :root {
    --red: #ec3b33;
    --white: #ffffff;
    --ink: #2e2e2e;
    --line: #555555;
    --page: #e4e4e4;
  }
  * { margin: 0; padding: 0; box-sizing: border-box; }
  html, body { width: 828px; height: 1200px; overflow: hidden; }
  body { background: var(--page); font-family: "Open Sans", sans-serif; position: relative; }

  .postcard { position: absolute; left: 73px; width: 682px; height: 489px; background: var(--red); overflow: hidden; box-shadow: 0 6px 14px rgba(0,0,0,.25); }
  .postcard--front { top: 79px; }
  .postcard--back { top: 643px; }
  .layer { position: absolute; left: 0; top: 0; }
  .abs { position: absolute; }

  /* front */
  .brand { left: 10px; top: 28px; width: 210px; text-align: center; }
  .brand__dot { display: block; width: 92px; height: 92px; margin: 0 auto 10px; border: 4px solid var(--red); border-radius: 50%; }
  .brand__name { color: var(--red); font-weight: 700; font-size: 20px; line-height: 1; }

  .coaching { right: 29px; top: 34px; text-align: right; color: var(--white); }
  .coaching__title { font-weight: 800; font-size: 34px; line-height: 36px; letter-spacing: .5px; }
  .coaching__sub { margin-top: 16px; font-weight: 600; font-size: 15px; line-height: 22px; }
  .coaching__list { list-style: none; margin-top: 10px; font-family: "Oswald", sans-serif; font-size: 18px; line-height: 25px; }
  .coaching__list li::before { content: "✓ "; }

  .price-row { right: 0; height: 43px; background: var(--white); color: var(--ink); display: flex; align-items: center; justify-content: flex-end; padding-right: 29px; gap: 10px; }
  .price-row--six { top: 262px; left: 398px; }
  .price-row--twelve { top: 307px; left: 388px; }
  .price-row__term { font-weight: 600; font-size: 20px; }
  .price-row__amount { font-weight: 800; font-size: 29px; }

  .special { right: 29px; top: 361px; text-align: right; color: var(--white); }
  .special__title { font-weight: 800; font-size: 30px; line-height: 34px; }
  .special__row { display: flex; align-items: center; gap: 6px; margin-top: 3px; }
  .special__note { font-family: "Oswald", sans-serif; font-size: 10px; line-height: 12px; }
  .special__save { background: var(--ink); font-family: "Oswald", sans-serif; font-weight: 600; font-size: 23px; padding: 0 10px; height: 34px; line-height: 34px; width: 121px; text-align: center; }

  .contact-bar { left: 0; top: 446px; width: 682px; height: 43px; display: flex; font-weight: 600; font-size: 15px; }
  .contact-bar > div { display: flex; align-items: center; justify-content: center; white-space: nowrap; }
  .contact-bar__web { width: 244px; background: var(--red); color: var(--white); }
  .contact-bar__mail { width: 231px; background: var(--ink); color: var(--white); font-size: 14px; }
  .contact-bar__phone { flex: 1; background: var(--white); color: var(--red); }

  /* back */
  .membership { left: 33px; top: 28px; color: var(--white); width: 290px; }
  .membership__title { font-weight: 800; font-size: 23px; line-height: 27px; }
  .membership__sub { font-weight: 600; font-size: 10.5px; margin-top: 6px; }
  .membership__list { list-style: none; margin-top: 6px; font-weight: 600; font-size: 14px; line-height: 20px; }
  .membership__list li::before { content: "✓ "; }

  .price-box { left: 33px; top: 179px; width: 236px; height: 76px; background: var(--white); border-radius: 5px; text-align: center; color: var(--red); padding-top: 5px; }
  .price-box__amount { font-family: "Anton", sans-serif; font-size: 38px; line-height: 46px; }
  .price-box__note { font-family: "Oswald", sans-serif; font-weight: 600; font-size: 14px; line-height: 16px; }

  .member-special { left: 33px; top: 262px; color: var(--white); font-weight: 700; font-size: 13px; line-height: 20px; }
  .member-special__title { font-weight: 800; font-size: 18px; line-height: 24px; }
  .member-special strong { font-size: 18px; font-weight: 800; }

  .opening-band { left: 0; top: 335px; width: 330px; height: 36px; background: var(--white); }
  .opening-band__text { position: absolute; left: 33px; top: 0; line-height: 36px; font-family: "Oswald", sans-serif; font-weight: 600; font-size: 21px; color: var(--ink); }

  .location { left: 33px; top: 379px; color: var(--white); }
  .location__date { font-weight: 700; font-size: 14px; line-height: 22px; }
  .location__address { font-weight: 600; font-size: 13.5px; line-height: 22px; display: flex; align-items: center; gap: 4px; }
  .location__more { font-weight: 600; font-size: 11px; line-height: 18px; }
  .location__contacts { display: grid; grid-template-columns: max-content max-content; column-gap: 20px; font-size: 12px; line-height: 17px; white-space: nowrap; }

  .stamp { left: 547px; top: 43px; width: 90px; height: 94px; border: 1px solid var(--line); }
  .address-line { left: 464px; width: 173px; height: 1px; background: var(--line); }
</style>
</head>
<body>

<section class="postcard postcard--front">
  <div class="price-row price-row--six abs"><span class="price-row__term">6months</span><span class="price-row__amount">$2500</span></div>
  <div class="price-row price-row--twelve abs"><span class="price-row__term">12months</span><span class="price-row__amount">$4500</span></div>

  <svg class="layer" width="682" height="446" viewBox="0 0 682 446">
    <defs>
      <linearGradient id="fairway" x1="0" y1="0" x2="0" y2="1">
        <stop offset="0" stop-color="#e9ebe4"/>
        <stop offset=".35" stop-color="#c9d3b8"/>
        <stop offset=".55" stop-color="#8ea85a"/>
        <stop offset="1" stop-color="#5f8a2a"/>
      </linearGradient>
    </defs>
    <path role="img" aria-label="Photo of a golf iron beside a ball on a tee on the fairway" d="M0,0 L285,0 Q498,224 326,446 L0,446 Z" fill="url(#fairway)"/>
    <path d="M299,0 Q514,224 340,446" fill="none" stroke="var(--white)" stroke-width="1.5"/>
  </svg>

  <div class="brand abs">
    <span class="brand__dot"></span>
    <span class="brand__name">Fairway Nine Golf</span>
  </div>

  <div class="coaching abs">
    <h1 class="coaching__title">OUR COACHING<br>PROGRAM</h1>
    <p class="coaching__sub">2 Lessons a Month<br>With Tour Quality Technology</p>
    <ul class="coaching__list">
      <li>Brightlane VX9</li>
      <li>Arcmotion Replay Studio</li>
      <li>ROLO GreenDesk</li>
    </ul>
  </div>

  <div class="special abs">
    <h2 class="special__title">SPECIAL</h2>
    <div class="special__row">
      <p class="special__note">PRE-PAY FOR A FULL-YEAR PROGRAM<br>BEFORE THE NEW YEAR AND</p>
      <span class="special__save">SAVE $500</span>
    </div>
  </div>

  <div class="contact-bar abs">
    <div class="contact-bar__web">www.fairwayninegolf.example</div>
    <div class="contact-bar__mail">info@fairwayninegolf.example</div>
    <div class="contact-bar__phone">513-862-7305</div>
  </div>
</section>

<section class="postcard postcard--back">
  <div class="opening-band abs"><span class="opening-band__text">Our New Location is Opening</span></div>

  <svg class="layer" width="682" height="489" viewBox="0 0 682 489">
    <path d="M410,0 L682,0 L682,489 L410,489 Q212,245 410,0 Z" fill="var(--white)"/>
    <path d="M396,0 Q194,245 396,489" fill="none" stroke="var(--white)" stroke-width="1.5"/>
  </svg>

  <div class="membership abs">
    <h2 class="membership__title">INDOOR<br>PRACTICE MEMBERSHIP</h2>
    <p class="membership__sub">practice indoors rain or shine with the use of Flightbox</p>
    <ul class="membership__list">
      <li>Combine practice</li>
      <li>Virtual driving range</li>
      <li>Golf courses</li>
    </ul>
  </div>

  <div class="price-box abs">
    <div class="price-box__amount">$200/month</div>
    <div class="price-box__note">Unlimited Practice Sessions.</div>
  </div>

  <div class="member-special abs">
    <div class="member-special__title">SPECIAL,</div>
    <div>pre-pay for the year and <strong>SAVE $400</strong></div>
    <div>plus get <strong>24/7</strong> access to practice.</div>
  </div>

  <div class="location abs">
    <div class="location__date">January 2020,</div>
    <div class="location__address">
      <svg width="10" height="13" viewBox="0 0 10 13" aria-hidden="true"><path d="M5,1 a3,3 0 1 1 0,6 a3,3 0 1 1 0,-6 M5,7 L5,10 M1,12 L9,12" fill="none" stroke="var(--white)" stroke-width="1.3"/></svg>
      4215B Marrow Hollis Avenue.
    </div>
    <div class="location__more">For more information and to sign up contact us at</div>
    <div class="location__contacts">
      <span>info@fairwayninegolf.example</span><span>513-862-7305</span>
      <span>www.fairwayninegolf.example</span>
    </div>
  </div>

  <div class="stamp abs"></div>
  <div class="address-line abs" style="top:237px"></div>
  <div class="address-line abs" style="top:288px"></div>
  <div class="address-line abs" style="top:339px"></div>
</section>

</body>
</html>
```